Web Design

We need a new website for our company. We perform several functions:

1 - IT and Network Support
2 - Computer Consultancy
3 - Cloud Services
4 - Hosted Mailvane & Online Backup
5 - Internet Connections & VOIP

Examples of some of the designs we like can be seen on:
• www.brelvox.com
• www.quintaro.com

I urgently need a new website to be designed to enable me to look more professional. My competitors website is www.tdmq.co.uk

I also want to be able to look much more professional, like www.brelvox.com www.quintaro.com

I have attached how I would like the website to look

Task outline
To design a home page and another internal skeleton page for a website following our requirements specification and wireframe layout/structure

Task description
We are looking for a modern, attractive, clean design for our new website to reflect our businesses professionalism and high quality services that we offer.
• www.brelvox.com
• www.quintaro.com
We would like a design for a home page and one other skeleton subpage for our website. We have provided a wireframe image to assist, showing how we would like the layout/structure of our website to follow which also highlights where we would like specific content/features to go.
We have listed what features the site must have in the requirements section.
The final design should communicate to our users that we are a professional business that offer high quality services and that we are a company they can trust and rely on.

Look and feel
The wireframe we have attached is a representation of how we would like the layout and structure of the website to be designed. We would like to have a corporate theme to our website.

Colours
Open to interpretation by the designer, as long as the colours suit a corporate theme and give off a professional look and feel.

Requirements
The design must have the following:

General
• Home page design (Based on attached wireframe).
• Internal Page design (This needs to be a skeleton page which can be used for implemented the content for all over pages).

• Contact details to be visible on every page, contact number at the header and all other relative details in the footer section.
• Social networking icons within the footer section of the site.
• Avoid the use of unprofessional images for buttons, icons and banners etc.
Features desired
• Drop down navigation bar. Please see the attached image for inspiration for its design/layout.
o We would like a similar drop down menu design to the one on this site: www.tdmq.co.uk.
• Image slider at the header of every page just beneath the navigation bar.
o We would like the Plexa slider to be used for the image slider. Please use this link for an example of it in action: http://www.scriptloomhub.net/demo/plexa-slider/
o The image slider needs to be larger on the home page.
o The image slider can be smaller on the rest of the pages of the site.
• Chirply feed present on every page.
• News/Blog feed present on every page.
• Call back form present on every page.
• Wayfindr Map implementation above footer on every page.

A user friendly, accessible design that is easy to use and easy for the user to understand. Must have a corporate theme to reflect the professionalism of our business. Content flows logically and keep content spaced out so that it does not make the site look cluttered.

Target Market(s)

Small to Mid sized Business, Large Banks and Legal, corporate, business - non-technical users

Industry/Entity Type

Business

Font styles to use
Sans Serif

```html
<!DOCTYPE html>
<html lang="en">
<head>
<meta charset="utf-8">
<title>Clydemere Systems — IT Support Glasgow</title>
<link href="https://fonts.googleapis.com/css2?family=Open+Sans:wght@400;600;700&display=swap" rel="stylesheet">
<style>
:root{
  --blue:#1f4aa8;
  --blue-dark:#163a87;
  --blue-bright:#3f7be0;
  --orange:#f7870f;
  --orange-dark:#e36a00;
  --text:#555b66;
  --muted:#8a8f98;
  --line:#d9dce2;
  --field:#eeeff1;
  --panel:#f2f2f2;
  --white:#ffffff;
  --map:#e3e3e3;
}
*{box-sizing:border-box;margin:0;padding:0}
html,body{width:1200px;height:2267px;overflow:hidden;background:var(--white)}
body{font-family:"Open Sans",Arial,sans-serif;color:var(--text);position:relative}
.abs{position:absolute}
a{color:inherit;text-decoration:none}

/* header */
.site-header{top:0;left:0;width:1200px;height:87px}
.brand{left:127px;top:24px;display:flex;align-items:center;gap:10px;font-size:24px;font-weight:600;color:var(--blue);letter-spacing:.5px}
.brand-dot{width:14px;height:14px;border-radius:50%;background:var(--blue)}
.call{right:128px;top:18px;display:flex;align-items:center;gap:10px}
.call-icon{width:46px;height:46px;border:3px solid var(--orange);border-radius:50%;display:flex;align-items:center;justify-content:center}
.call-text{font-weight:700;line-height:1.15}
.call-text .label{color:var(--blue);font-size:18px}
.call-text .num{color:var(--orange);font-size:21px}

/* nav */
.main-nav{top:87px;left:0;width:1200px;height:49px;background:linear-gradient(#4a86ea,var(--blue-bright) 40%,#2d63c7)}
.nav-list{left:127px;top:0;display:flex;list-style:none;height:49px}
.nav-list li{color:#fff;font-size:13px;font-weight:600;text-transform:uppercase;padding:0 44px;line-height:49px;border-left:1px solid rgba(255,255,255,.35)}
.nav-list li:first-child{border-left:none;padding-left:44px}
.nav-social{right:128px;top:14px;display:flex;gap:16px;color:#fff;font-size:14px;font-weight:700}

/* hero */
.hero{top:136px;left:0;width:1200px;height:382px;background:radial-gradient(ellipse at 50% 55%,#3a5f8c 0%,#17324f 45%,#0a1524 80%)}
.hero-side{top:0;height:382px;width:300px}
.hero-side.left{left:0;background:linear-gradient(90deg,#2d6ca6 0%,rgba(40,90,140,.2) 100%)}
.hero-side.right{right:0;background:linear-gradient(270deg,#cfe6f5 0%,rgba(120,170,210,.4) 40%,rgba(20,40,70,0) 100%)}
.hero-copy{left:0;top:30px;width:1200px;text-align:center;color:#fff;font-size:28px;line-height:1.3;font-weight:400}
.hero-copy strong{font-weight:700;font-size:32px}
.hero-btn{left:510px;top:122px;width:183px;height:44px;border-radius:22px;background:linear-gradient(var(--orange),var(--orange-dark));color:#fff;font-weight:600;font-size:17px;text-align:center;line-height:44px;box-shadow:0 2px 4px rgba(0,0,0,.4)}
.slider-dots{top:546px;left:552px;display:flex;gap:4px;align-items:center}
.slider-dots span{width:11px;height:11px;border-radius:50%;background:#c7c8cb}
.slider-dots .on{width:15px;height:15px;background:#fff;border:3px solid #6d7078}

/* welcome */
h2{font-size:27px;font-weight:700;color:var(--orange)}
h2 .alt{color:var(--blue)}
.welcome{left:127px;top:585px;width:618px}
.welcome p{font-size:11.6px;line-height:15.4px;margin-top:18px;text-align:justify;color:#6a6f78}
.welcome h2{margin-bottom:4px}

/* chirply widget */
.feed{left:778px;top:593px;width:293px;height:331px;border:1px solid var(--line);background:#fff;padding:8px}
.feed-head{height:46px;background:linear-gradient(#5b8fe8,var(--blue));display:flex;align-items:center;padding:0 8px;gap:10px;color:#fff;font-size:12px;line-height:1.2}
.feed-avatar{width:40px;height:28px;background:#2d5cb4;border:1px solid #8fb1ee}
.tweet{font-size:11.6px;line-height:17px;color:var(--blue);padding:10px 0 6px;border-bottom:1px dotted #9aa0aa}
.tweet .tag{color:var(--blue)}
.tweet .meta{color:var(--orange);display:block}
.feed-foot{margin-top:8px;height:46px;background:var(--orange);display:flex;align-items:center;justify-content:space-between;padding:0 12px;color:#fff}
.feed-foot .name{font-weight:700;font-size:18px}
.feed-foot .cta{font-size:12px}

/* contact form */
.callback{left:778px;top:950px;width:293px}
.callback h3{display:flex;align-items:center;gap:10px;font-size:17px;font-weight:400;color:var(--orange);text-transform:uppercase;margin-bottom:10px}
.callback h3 .alt{color:var(--blue)}
.field{height:36px;background:var(--field);margin-bottom:8px;font-size:12px;color:#555;padding:8px}
.field.msg{height:122px}
.send{margin-top:10px;width:126px;height:36px;border-radius:18px;background:linear-gradient(#4c87ea,var(--blue));border:2px solid #8db0ee;color:#fff;font-size:13px;text-align:center;line-height:32px;box-shadow:0 1px 3px rgba(0,0,0,.35)}

/* testimonials */
.clients-head{left:127px;top:1252px;width:618px;display:flex;justify-content:space-between;align-items:baseline}
.clients-head .all{font-size:11.6px;color:var(--orange);text-decoration:underline}
.testimonials{left:127px;top:1317px;width:618px;height:336px;background:linear-gradient(135deg,#e4e4e4,#fafafa 45%,#e6e6e6);border:1px solid #ddd;border-radius:4px}
.quote{position:absolute;left:20px;width:580px;display:flex;gap:24px}
.quote-photo{width:124px;height:104px;border:5px solid #fff;box-shadow:0 2px 4px rgba(0,0,0,.3);flex:none}
.quote-photo.city{background:linear-gradient(160deg,#cfe3f5,#6f97bf 60%,#38597d);transform:rotate(-3deg)}
.quote-photo.person{background:linear-gradient(160deg,#f29a3a,#d4681d 55%,#5a3a2a);transform:rotate(-3deg)}
.quote-body{font-size:12px;line-height:16px;color:#6a6f78;padding-top:8px}
.quote-body .more{color:var(--orange)}
.quote-by{margin-top:20px;color:var(--blue)}
.quote-by em{color:var(--orange)}
.quote-rule{position:absolute;left:20px;right:20px;top:160px;height:1px;background:#c6c6c6}

/* news */
.news{left:778px;top:1317px;width:293px;height:336px;border:1px solid var(--line);padding:6px;background:#fff}
.news-head{height:46px;background:linear-gradient(var(--orange),var(--orange-dark));display:flex;align-items:center;gap:12px;padding:0 10px;color:#fff;font-size:16px;text-transform:uppercase}
.news-item{display:flex;gap:12px;padding:10px 0;border-bottom:1px solid #c9ccd2;height:83px}
.news-thumb{width:66px;height:52px;flex:none;background:linear-gradient(#f4f4f4,#dcdcdc);border:1px solid #ddd}
.news-item h4{font-size:12px;font-weight:600;color:var(--blue);white-space:nowrap}
.news-item p{font-size:11.6px;line-height:16px;color:#6a6f78;margin-top:4px}
.news-item p span{color:var(--orange)}
.news-all{text-align:right;font-size:11.6px;color:var(--orange);margin-top:14px}

/* partners */
.partners{left:127px;top:1712px;width:944px;display:flex;justify-content:space-between;align-items:center}
.badge{height:48px;background:#4a4a4a}
.badge.light{background:#d6d6d6}
.badge.round{border-radius:50%;width:48px}

/* map */
.map{left:0;top:1808px;width:1200px;height:355px;background:linear-gradient(160deg,#ececec,#dcdcdc 60%,#e6e6e6)}
.map-label{left:155px;top:1936px;font-size:15px;font-weight:600;color:var(--blue)}
.to-top{left:1018px;top:2122px;width:53px;height:53px;background:var(--orange);display:flex;align-items:center;justify-content:center}

/* footer */
.site-footer{left:0;top:2163px;width:1200px;height:104px;background:var(--blue);color:#fff}
.foot-contact{left:127px;top:22px;font-size:12px;line-height:16px}
.foot-contact h5{font-size:15px;font-weight:700;margin-bottom:10px;text-transform:uppercase}
.foot-cols{display:flex;gap:60px}
.foot-div{top:22px;width:1px;height:64px;background:rgba(255,255,255,.4)}
.foot-follow{left:622px;top:22px;width:150px;font-size:15px;font-weight:700;text-align:center}
.foot-follow .icons{display:flex;justify-content:center;gap:8px;margin-top:12px;font-size:11px;white-space:nowrap}
.foot-legal{right:128px;top:54px;font-size:11.5px;white-space:nowrap}
</style>
</head>
<body>

<header class="site-header abs">
  <div class="brand abs"><span class="brand-dot"></span>Clydemere Systems</div>
  <div class="call abs">
    <div class="call-icon">
      <svg width="24" height="24" viewBox="0 0 24 24"><path d="M6.6 10.8a15 15 0 0 0 6.6 6.6l2.2-2.2c.3-.3.7-.4 1-.2 1.1.4 2.3.6 3.6.6.6 0 1 .4 1 1V20c0 .6-.4 1-1 1A17 17 0 0 1 3 4c0-.6.4-1 1-1h3.5c.6 0 1 .4 1 1 0 1.3.2 2.5.6 3.6.1.3 0 .7-.2 1z" fill="#f7870f"/></svg>
    </div>
    <div class="call-text"><div class="label">Contact us now!</div><div class="num">0141 555 0287</div></div>
  </div>
</header>

<nav class="main-nav abs">
  <ul class="nav-list abs"><li>Home</li><li>Products</li><li>Company</li><li>Blogs</li></ul>
  <div class="nav-social abs"><span>Facelink</span><span>Chirply</span><span>Linkora</span></div>
</nav>

<section class="hero abs" role="img" aria-label="Banner photo: IT consultant seated among trading monitors">
  <div class="hero-side left abs"></div>
  <div class="hero-side right abs"></div>
  <p class="hero-copy abs"><strong>Lorem Ipsum</strong> is simply dummy text of<br>the printing and typesetting</p>
  <a class="hero-btn abs">READ MORE</a>
</section>
<div class="slider-dots abs"><span></span><span></span><span class="on"></span><span></span><span></span></div>

<main>
  <section class="welcome abs">
    <h2>Welcome to <span class="alt">Clydemere Systems</span></h2>
    <p>For many companies today, IT support is a large part of doing business. It is not always possible for a company or business to have a dedicated IT support team. For companies/businesses in Glasgow, Scotland, the answer for IT needs is Clydemere Systems Limited.</p>
    <p>With Clydemere Systems Limited, a client has the full expertise of a highly skilled team of network and infrastructure engineers to monitor and manage their network. Not only do the IT consultants of Clydemere Systems troubleshoot issues as they arise, but they also go the extra step of forecasting and assessing the risks of the network infrastructure. This proactive disaster management effort has garnered Clydemere Systems Limited business IT contracts from both the private and public sectors, as well as gaining Clydemere Systems Limited Nortiva Gold Certified Partner status. Besides offering business IT support services in the Glasgow area, Clydemere Systems Limited offers a number of services such as online backup and recovery, hosted mail/exchange and cloud computing, to name a few.</p>
    <p>Clydemere Systems Limited offers three varieties of backup support: tape, disk/hard drive, and online backup. Tape and disk backups are excellent recovery strategies for a business on site, but online backup, via the Clydemere Systems Limited cloud, can offer businesses a mobile, reliable and fault tolerant solution. Offsite cloud recovery saves a business investing in local hardware and in the case of a total catastrophe, the enduring corporate data resides safely offsite in a fail over storage environment.</p>
    <p>The business workspace today is no longer a bricks and mortar office; most business is done outside of the actual company location. To enable clients to compete with the mobile market, Clydemere Systems limited offers hosted email services. Featuring Nortiva Mailvane 2010, employees can access a company's email service via Postdeck, on mobile devices or via a web portal. A hosted email solution ensures employees have access on the road or with a home office arrangement. Safe, reliable and scalable, like online backup and recovery, hosted email requires no hardware or infrastructure investment by the client.</p>
    <p>As previously mentioned, Clydemere Systems Limited offers a range of cloud computing services to clients. Besides offering hosted email, online backups, Clydemere Systems Limited offers cloud threat protection. Cloud based anti-virus ensures that all devices connected to a client's network have the latest virus signature files, and requires no intervention by the user. As soon as there is an incident, alerts are generated and dealt with swiftly to ensure the integrity of a client's network.</p>
    <p>When considering a provider to manage and administer a company's technology needs, consider the one that utilizes leading edge technology to ensure subscribers are competitive and best equipped to deal with the changing face of business. Consider Clydemere Systems Limited.</p>
  </section>

  <aside class="feed abs">
    <div class="feed-head"><span class="feed-avatar"></span><span>Clydemere Systems<br>clydemere_IT</span></div>
    <div class="tweet">clydemere_IT New server going in, new customers in <span class="tag">#glasgow</span> and <span class="tag">#hamilton</span> . Exciting times! -<span class="meta">3 months · reply · retweet · favorite</span></div>
    <div class="tweet">clydemere_IT New server going in, new customers in <span class="tag">#glasgow</span> and <span class="tag">#hamilton</span> . Exciting times! -<span class="meta">3 months · reply · retweet · favorite</span></div>
    <div class="tweet">clydemere_IT New server going in, new customers in <span class="tag">#glasgow</span> and <span class="tag">#hamilton</span> . Exciting times! -<span class="meta">3 months · reply · retweet · favorite</span></div>
    <div class="feed-foot"><span class="name">Chirply</span><span class="cta">Join the conversation</span></div>
  </aside>

  <section class="callback abs">
    <h3>
      <svg width="26" height="22" viewBox="0 0 26 22"><rect x="1" y="5" width="17" height="15" fill="none" stroke="#8a8f98" stroke-width="1.5"/><path d="M9 15l2-5L22 1l3 3-11 9z" fill="#f7870f"/></svg>
      <span>Contact <span class="alt">Us</span></span>
    </h3>
    <div class="field">Name:</div>
    <div class="field">Email:</div>
    <div class="field">Phone:</div>
    <div class="field msg">Message:</div>
    <div class="send">Send</div>
  </section>

  <div class="clients-head abs"><h2>What Our <span class="alt">Clients Say</span></h2><a class="all">View All Testimonials</a></div>
  <section class="testimonials abs">
    <div class="quote" style="top:24px">
      <div class="quote-photo city" role="img" aria-label="Photo of office towers"></div>
      <div class="quote-body">Consistently supplied a high level of service and available 24/7. I would recommend them to anyone looking for an expert service provider.<br><span class="more">Read More [...]</span>
        <div class="quote-by">Martin – <em>Stonegate Business Services Ltd</em></div></div>
    </div>
    <div class="quote-rule"></div>
    <div class="quote" style="top:196px">
      <div class="quote-photo person" role="img" aria-label="Client portrait"></div>
      <div class="quote-body">IT experts who talk in everyday language and very helpful. Clydemere Systems offers a wide range of IT services and I have always found them approachable and quick to react. <span class="more">Read More [...]</span>
        <div class="quote-by">Graham Lowrie – <em>Kestrel Motors UK</em></div></div>
    </div>
  </section>

  <aside class="news abs">
    <div class="news-head">
      <svg width="34" height="28" viewBox="0 0 34 28"><rect x="1" y="1" width="32" height="26" rx="3" fill="none" stroke="#fff" stroke-width="2"/><rect x="6" y="7" width="9" height="8" fill="#fff"/><path d="M19 8h9M19 13h9M6 20h22" stroke="#fff" stroke-width="2"/></svg>
      <span>Latest News</span>
    </div>
    <div class="news-item"><div class="news-thumb" role="img" aria-label="News thumbnail"></div><div><h4>Why Our Competitors Hate Us...</h4><p>When you hire IT Consultants from us, we give you <span>[...]</span></p></div></div>
    <div class="news-item"><div class="news-thumb" role="img" aria-label="News thumbnail"></div><div><h4>Why Our Competitors Hate Us...</h4><p>When you hire IT Consultants from us, we give you <span>[...]</span></p></div></div>
    <div class="news-item"><div class="news-thumb" role="img" aria-label="News thumbnail"></div><div><h4>Why Our Competitors Hate Us...</h4><p>When you hire IT Consultants from us, we give you <span>[...]</span></p></div></div>
    <div class="news-all">See All News &gt;&gt;</div>
  </aside>

  <div class="partners abs" aria-label="Partner accreditations">
    <span class="badge" style="width:82px"></span>
    <span class="badge" style="width:68px"></span>
    <span class="badge light" style="width:60px"></span>
    <span class="badge light" style="width:96px;height:30px"></span>
    <span class="badge light" style="width:50px"></span>
    <span class="badge light" style="width:86px;height:40px"></span>
    <span class="badge light" style="width:76px"></span>
    <span class="badge round"></span>
  </div>
</main>

<section class="map abs" role="img" aria-label="Wayfindr Map showing the office location near Dalry"></section>
<svg class="abs" style="left:184px;top:1872px" width="40" height="56" viewBox="0 0 40 56"><path d="M20 0C9 0 0 9 0 20c0 15 20 36 20 36s20-21 20-36C40 9 31 0 20 0z" fill="#d8281e"/><circle cx="20" cy="19" r="7" fill="#9c140d"/></svg>
<div class="map-label abs">Clydemere Systems</div>
<a class="to-top abs" aria-label="Back to top"><svg width="22" height="22" viewBox="0 0 22 22"><path d="M11 2L20 20L11 15L2 20z" fill="#fff"/></svg></a>

<footer class="site-footer abs">
  <div class="foot-contact abs">
    <h5>Contact Information</h5>
    <div class="foot-cols">
      <div>Clydemere Systems Limited<br>14-16 Mill Lane, Dalry, KA24 9QX</div>
      <div>T. +44(0)141 5550287<br>hello@clydemere-systems.example</div>
    </div>
  </div>
  <div class="foot-div abs" style="left:603px"></div>
  <div class="foot-follow abs">Follow us on<div class="icons"><span>Facelink</span><span>Chirply</span><span>Linkora</span></div></div>
  <div class="foot-div abs" style="left:790px"></div>
  <div class="foot-legal abs">Privacy | Sitemap | Copyright © 2014Clydemere</div>
</footer>

</body>
</html>
```